Post Card Invitation to Wedding Rehearsal Dinner and After Party

This post card should serve as invitations for two events in the wedding weekend for two San Francisco grooms, Derek and Simon.
Each side of the card should have distinct looks and information but tied together with “Before” on the front and “After” on the back.
POST CARD FRONT
Required text:
BEFORE
Derek and Simon’s Wedding: Rehearsal Dinner
Friday, May 22, 2015
5:30 PM
Larkvale Grub Yard
617 Tessler Avenue @ Marlow
San Francisco, CA
Please also convey the following information without necessarily quoting directly: This rehearsal dinner will be held in a private enclosed space in the food truck park. We we will serve beer and wine in our space and provide tickets to purchase food from any of the trucks in the park. Dress is casual.
Look and feel of the card should have a modern, “hipster” feel to it. If you search Google images for “Hipster design” or “hipster infographic” you should get a sense of the overall design and colors. The website for the venue is http://larkvalegrubyard.com/ for reference but please DO NOT use any images or logos from the site.
----------------------
POST CARD REVERSE
Required Text:
AFTER
Derek and Simon’s Wedding: After Party
Saturday, May 23, 2015
7:30 PM
Corvell Harbor Sailing Club
42 Pennick Lane
San Francisco, CA
Please also convey the following information without necessarily quoting directly: Black-tie optional. Dancing, snacks and dessert and cocktails with panoramic views of the San Francisco Bay and Golden Gate Bridge.
This should have a much different look and feel from the front of the card. It should convey an elegant black-tie affair. If you search Google images for “black tie after party invitation” you should get some examples of an overall feel that I am aiming for. The website for the venue is www.chsclub.com but DO NOT use any of the images or logos from the site.
Industry/Entity Type
Wedding
Look and feel
Each slider illustrates characteristics of the customer's brand and the style your logo design should communicate.

```html
<!DOCTYPE html>
<html lang="en">
<head>
<meta charset="utf-8">
<title>Derek &amp; Simon – Rehearsal Dinner and After Party Invitations</title>
<link rel="stylesheet" href="https://fonts.googleapis.com/css2?family=Kaushan+Script&family=Montserrat:wght@800&family=Josefin+Sans:wght@300&family=Shadows+Into+Light&family=Questrial&family=Parisienne&family=Cormorant+Garamond:wght@400&family=Raleway:wght@300&display=swap">
<style>
  :root {
    --backdrop: #5d4737;
    --paper: #ffffff;
    --ink: #111111;
    --night: #050505;
    --silver: #e6e6e6;
    --ornament-light: #f2f2f2;
    --ornament-dim: #8c8c8c;
    --crown-tone: #1a1a1a;
  }
  * { margin: 0; padding: 0; box-sizing: border-box; }
  html, body { width: 1200px; height: 1000px; overflow: hidden; }
  body { position: relative; background: var(--backdrop); }

  .card { position: absolute; top: 143px; height: 842px; overflow: hidden; }
  .card > * { position: absolute; }
  .centered { left: 0; width: 100%; text-align: center; transform: translateY(-50%); line-height: 1; }

  /* ---------- Front: rehearsal dinner ---------- */
  .card--before { left: 38px; width: 565px; background: var(--paper); color: var(--ink); }
  .before-art { left: 0; top: 0; width: 565px; height: 842px; }
  .monogram-date { font-family: "Questrial", sans-serif; font-size: 17px; letter-spacing: 1px; left: 240px; width: 60px; text-align: center; transform: translateY(-50%); line-height: 1; }
  .monogram-names { font-family: "Josefin Sans", sans-serif; font-weight: 300; font-size: 25px; left: 120px; width: 300px; text-align: center; transform: translateY(-50%); top: 146px; line-height: 1; white-space: nowrap; }
  .event-word--before { font-family: "Kaushan Script", cursive; font-size: 58px; top: 290px; }
  .event-title { font-family: "Questrial", sans-serif; font-size: 20px; top: 355px; }
  .date-day { font-family: "Shadows Into Light", cursive; font-size: 74px; left: 28px; top: 433px; transform: translateY(-50%); line-height: 1; letter-spacing: 2px; }
  .date-num { font-family: "Montserrat", sans-serif; font-weight: 800; font-size: 34px; left: 232px; width: 80px; text-align: center; top: 439px; transform: translateY(-50%); line-height: 1; }
  .date-suffix { font-family: "Montserrat", sans-serif; font-weight: 800; font-size: 15px; left: 323px; top: 396px; line-height: 1; }
  .date-of { font-family: "Questrial", sans-serif; font-size: 15px; left: 328px; top: 433px; line-height: 1; }
  .date-month { font-family: "Montserrat", sans-serif; font-weight: 800; font-size: 62px; left: 356px; top: 437px; transform: translateY(-50%); line-height: 1; }
  .event-time { font-family: "Questrial", sans-serif; font-size: 48px; left: 32px; top: 575px; transform: translateY(-50%); line-height: 1; letter-spacing: 1px; }
  .venue-name { font-family: "Shadows Into Light", cursive; font-size: 32px; left: 320px; width: 200px; text-align: center; top: 586px; transform: translateY(-50%); line-height: 36px; }
  .venue-address { font-family: "Questrial", sans-serif; font-size: 20px; left: 0; width: 540px; text-align: center; top: 650px; line-height: 23px; }
  .crown { background: var(--crown-tone); border-radius: 6px 6px 2px 2px; }
  .crown--tall { left: 62px; top: 705px; width: 152px; height: 84px; }
  .crown--round { left: 347px; top: 716px; width: 110px; height: 70px; border-radius: 40px 40px 4px 4px; }

  /* ---------- Back: after party ---------- */
  .card--after { left: 622px; width: 543px; background: var(--night); color: var(--silver); }
  .after-art { left: 0; top: 0; width: 543px; height: 842px; }
  .flourish { background: linear-gradient(180deg, var(--ornament-light), var(--ornament-dim)); opacity: .85; }
  .flourish--top-band { left: 18px; top: 6px; width: 508px; height: 56px; border-radius: 28px 28px 10px 10px; }
  .flourish--bottom-band { left: 18px; top: 762px; width: 508px; height: 74px; border-radius: 10px 10px 28px 28px; }
  .flourish--crest-top { left: 229px; top: 100px; width: 84px; height: 34px; border-radius: 40px 40px 6px 6px; }
  .flourish--crest-bottom { left: 229px; top: 228px; width: 84px; height: 42px; border-radius: 6px 6px 40px 40px; }
  .flourish--divider-top { left: 160px; top: 488px; width: 226px; height: 14px; border-radius: 7px; }
  .flourish--divider-bottom { left: 160px; top: 732px; width: 226px; height: 14px; border-radius: 7px; }
  .couple-script { font-family: "Parisienne", cursive; font-size: 48px; top: 186px; color: var(--paper); white-space: nowrap; }
  .event-word--after { font-family: "Cormorant Garamond", serif; font-size: 42px; top: 348px; color: var(--paper); }
  .event-title--script { font-family: "Parisienne", cursive; font-size: 27px; top: 428px; color: var(--paper); white-space: nowrap; }
  .party-details { left: 0; width: 100%; text-align: center; top: 534px; font-family: "Raleway", sans-serif; font-weight: 300; font-size: 25px; line-height: 33.8px; list-style: none; }
</style>
</head>
<body>

<section class="card card--before" aria-label="Rehearsal dinner invitation">
  <svg class="before-art" viewBox="0 0 565 842" aria-hidden="true" fill="none" stroke="var(--ink)" stroke-width="2.5" stroke-linecap="round">
    <polygon points="97,144 270,62 445,144 270,226"/>
    <polygon points="116,144 270,73 426,144 270,215" stroke-width="2"/>
    <line x1="270" y1="25" x2="270" y2="46"/>
    <line x1="270" y1="238" x2="270" y2="259"/>
    <line x1="157" y1="79" x2="172" y2="94"/>
    <line x1="383" y1="79" x2="368" y2="94"/>
    <line x1="157" y1="210" x2="172" y2="195"/>
    <line x1="383" y1="210" x2="368" y2="195"/>
    <line x1="30" y1="144" x2="82" y2="144"/>
    <path d="M30,144 L46,137 L58,144 L46,151 Z" fill="var(--ink)"/>
    <line x1="457" y1="144" x2="507" y2="144"/>
    <path d="M509,144 L492,135 M509,144 L492,153" stroke-width="3"/>
    <line x1="30" y1="294" x2="168" y2="294"/>
    <path d="M170,294 L154,286 L154,302 Z" fill="var(--ink)"/>
    <path d="M32,286 L42,294 L32,302 M42,286 L52,294 L42,302 M52,286 L62,294 L52,302" stroke-width="2"/>
    <line x1="372" y1="294" x2="512" y2="294"/>
    <path d="M370,294 L386,286 L386,302 Z" fill="var(--ink)"/>
    <path d="M510,286 L500,294 L510,302 M500,286 L490,294 L500,302 M490,286 L480,294 L490,302" stroke-width="2"/>
    <polygon points="272,385 317,411 317,463 272,489 227,463 227,411" stroke-width="2"/>
    <circle cx="272" cy="437" r="33" stroke-width="3"/>
    <line x1="17" y1="500" x2="512" y2="500" stroke-width="2"/>
    <line x1="17" y1="507" x2="512" y2="507" stroke-width="2"/>
    <line x1="17" y1="514" x2="512" y2="514" stroke-width="2"/>
    <line x1="226" y1="527" x2="307" y2="627" stroke-width="2"/>
    <line x1="308" y1="527" x2="227" y2="627" stroke-width="2"/>
    <path d="M224,524 L226,540 M224,524 L239,528" stroke-width="2.5"/>
    <path d="M310,524 L308,540 M310,524 L295,528" stroke-width="2.5"/>
    <path d="M300,619 L310,617 M303,624 L313,622 M234,619 L224,617 M231,624 L221,622" stroke-width="2"/>
    <circle cx="267" cy="577" r="9" stroke-width="2"/>
  </svg>

  <span class="monogram-date" style="top:97px">05</span>
  <span class="monogram-names">DEREK &amp; SIMON</span>
  <span class="monogram-date" style="top:193px">22</span>

  <h1 class="centered event-word--before" style="font-weight:400">before</h1>
  <p class="centered event-title">Derek and Simon’s Wedding: Rehearsal Dinner</p>

  <span class="date-day">friday</span>
  <span class="date-num">22</span>
  <span class="date-suffix">ND</span>
  <span class="date-of">Of</span>
  <span class="date-month">MAY</span>

  <span class="event-time">5:30 PM</span>
  <span class="venue-name">Larkvale Grub Yard</span>
  <p class="venue-address">617 Tessler Avenue @ Marlow<br>San Francisco, CA</p>

  <div class="crown crown--tall" role="img" aria-label="Black crown illustration"></div>
  <div class="crown crown--round" role="img" aria-label="Black rounded crown illustration with fleur-de-lis"></div>
</section>

<section class="card card--after" aria-label="After party invitation">
  <svg class="after-art" viewBox="0 0 543 842" aria-hidden="true" stroke="var(--paper)" stroke-width="3" stroke-linecap="round" fill="var(--paper)">
    <line x1="60" y1="125" x2="484" y2="125"/>
    <circle cx="58" cy="125" r="3.5"/>
    <circle cx="486" cy="125" r="3.5"/>
    <line x1="60" y1="237" x2="484" y2="237"/>
    <circle cx="58" cy="237" r="3.5"/>
    <circle cx="486" cy="237" r="3.5"/>
  </svg>

  <div class="flourish flourish--top-band" role="img" aria-label="White ornamental scrollwork border"></div>
  <div class="flourish flourish--crest-top" role="img" aria-label="White scroll ornament"></div>
  <h2 class="centered couple-script" style="font-weight:400">Derek and Simon</h2>
  <div class="flourish flourish--crest-bottom" role="img" aria-label="White scroll ornament"></div>

  <h1 class="centered event-word--after" style="font-weight:400">after</h1>
  <p class="centered event-title--script">Derek and Simon’s Wedding: After Party</p>

  <div class="flourish flourish--divider-top" role="img" aria-label="Thin white flourish divider"></div>
  <ul class="party-details">
    <li>Saturday, May 23, 2015</li>
    <li>7:30 PM</li>
    <li>Corvell Harbor Sailing Club</li>
    <li>42 Pennick Lane</li>
    <li>San Francisco, CA</li>
  </ul>
  <div class="flourish flourish--divider-bottom" role="img" aria-label="Thin white flourish divider"></div>
  <div class="flourish flourish--bottom-band" role="img" aria-label="White ornamental scrollwork border"></div>
</section>

</body>
</html>
```